R&T Architects - business card and stationary

Aloha,

We have a simple text logo, we need it incorporated into a business card and also stationary design (letterhead) if possible.

Please check out our website, rtamaui-studio.example for a little more about us. The logo we would like to use is in the upper left corner of the website. It is a simple colored logo based on the Klavica font. We are open to new logo's as well, but we want simple.

Thanks

```html
<!DOCTYPE html>
<html lang="en">
<head>
<meta charset="utf-8">
<title>R&amp;T Architects — Business Card</title>
<link href="https://fonts.googleapis.com/css2?family=Saira+Semi+Condensed:wght@700&family=Mulish:wght@400;800&display=swap" rel="stylesheet">
<style>
  :root {
    --backdrop: #ebe8e1;
    --card: #ffffff;
    --brand-green: #8fb33c;
    --earth-brown: #6a5a36;
    --sand: #c3b38f;
    --rule: #b9ab8a;
  }
  * { margin: 0; padding: 0; box-sizing: border-box; }
  html, body {
    width: 1200px;
    height: 900px;
    overflow: hidden;
    background: var(--backdrop);
  }
  .business-card {
    position: absolute;
    left: 60px;
    top: 132px;
    width: 1082px;
    height: 618px;
    background: var(--card);
  }
  .wordmark {
    position: absolute;
    left: 86px;
    top: 100px;
    font-family: "Saira Semi Condensed", "Arial Narrow", sans-serif;
    font-weight: 700;
    font-size: 100px;
    line-height: 1;
    color: var(--brand-green);
    text-transform: uppercase;
    white-space: nowrap;
  }
  .holder-name {
    position: absolute;
    left: 90px;
    top: 222px;
    font-family: "Saira Semi Condensed", "Arial Narrow", sans-serif;
    font-weight: 700;
    font-size: 40px;
    letter-spacing: 2px;
    line-height: 1;
    color: var(--sand);
    text-transform: uppercase;
    white-space: nowrap;
  }
  .contact-line {
    position: absolute;
    left: 0;
    right: 0;
    top: 528px;
    display: flex;
    align-items: center;
    gap: 12px;
    font-family: "Mulish", sans-serif;
    font-size: 22px;
    line-height: 1;
    color: var(--earth-brown);
    white-space: nowrap;
  }
  .contact-line .edge-bar {
    flex: 1 1 20px;
    min-width: 12px;
    height: 14px;
    background: var(--sand);
  }
  .contact-item .label {
    font-weight: 800;
    text-transform: uppercase;
    margin-right: 5px;
  }
  .contact-line .divider {
    width: 1.5px;
    height: 26px;
    background: var(--rule);
  }
</style>
</head>
<body>
  <section class="business-card">
    <div class="wordmark">R&amp;T Architects</div>
    <div class="holder-name">Noah Kealoha</div>
    <div class="contact-line">
      <span class="edge-bar"></span>
      <span class="contact-item"><span class="label">Phone:</span>808.555.0142</span>
      <span class="divider"></span>
      <span class="contact-item"><span class="label">Email:</span>noah@rtamaui-studio.example</span>
      <span class="divider"></span>
      <span class="contact-item"><span class="label">Internet:</span>rtamaui-studio.example</span>
      <span class="edge-bar"></span>
    </div>
  </section>
</body>
</html>
```